Software Application page - product section

I have developed a proposal generation application and want to improve the main user interface page.
This is the most important and most used page within my application and therefore it needs to look slick, clean, simple and easy to understand whilst looking very professional, creditable and established.
This is the page in which the user makes certain selections of products and the system will in turn display information on the product selected. The user can then add the product to the basket and the system also calculates the monthly cost of the product along with the profit the user makes by offering the particular product.
I have put something together myself and uploaded accordingly to give you an idea as to what it currently looks like and the structure that it needs to follow.
Section 1
This displays the Customer's account, proposal ID, Customer name etc
Section 2
I have these as radio buttons that the user selects, then clicks on the 'Search product' button. The items will then be displayed in section 3
Section 3
This datagrid displays the available products based on the section 2's selections
Section 4
shows information on the product that has been highlighed in section 3's datagrid. The user then clicks in qty field to enter the qty and then clicks the ADD shopping basket button to add the product to the basket in section 5 datagrid.
Section 5
This is the datagrid/shopping basket that displays all the products that the user has added.
Section 6
Displays all the figures including the total qtys', costs, revenue etc
WHILST IT IS IMPORTANT THAT THE DESIGN MUST FOLLOW THE STRUCTURE OF WHAT IS ATTACHED. I MUST POINT OUT THAT I AM NOT HAPPY WITH THE CURRENT DESIGN. I DO NOT LIKE THE LOOK AND FEEL OF THE CURRENT DESIGN AS IT LOOKS CHEAP AND AMATEURISH.
THE RADIO BUTTONS IN SECTION 1 FOR EXAMPLE SHOULD BE MORE CREATIVE, THE SIZE OF EACH SECTIONS CURRENTLY LOOK DISPROPORTIONATE. THE COLOURS ARE ALL OVER THE PLACE.
THE SIZE OF PAGE MUST BE 1009 X 689
PLEASE VISIT OUT OUR WEBSITE TO STICK TO THE COMPANIES BRAND: www.velmodane.co.uk
I have other pages within my application that require designs along with icons and a lot of work on the website also require redesigning so the best design will also be given this work
Many thanks
Gareth
Software

```html
<!DOCTYPE html>
<html lang="en">
<head>
<meta charset="utf-8">
<title>Velmodane – Proposal Products</title>
<link href="https://fonts.googleapis.com/css2?family=Roboto:wght@400;500;700&display=swap" rel="stylesheet">
<style>
:root{
  --page-bg:#e8c8ee;
  --brand:#7f5587;
  --brand-line:#9470a0;
  --surface:#f9f9f9;
  --panel:#f2f2f2;
  --panel-line:#dcdcdc;
  --row-line:#e6e6e6;
  --field:#ffffff;
  --search:#e4e4e4;
  --scroll:#d6d6d6;
  --text:#333333;
  --muted-btn:#7a7a7a;
  --white:#ffffff;
}
*{box-sizing:border-box;margin:0;padding:0}
html,body{width:1200px;height:1092px;overflow:hidden;background:var(--page-bg);font-family:"Roboto",Helvetica,Arial,sans-serif;color:var(--text)}
.stage{position:absolute;left:0;top:0;width:1119px;height:1018px;transform:scale(1.0724);transform-origin:0 0}
.abs{position:absolute}
.app{position:absolute;left:55px;top:54px;width:1009px;height:908px;background:var(--surface);box-shadow:0 1px 4px rgba(0,0,0,.12)}
.topbar{position:absolute;left:0;top:0;width:1009px;height:51px;background:var(--brand);display:flex}
.brand{width:179px;height:51px;background:#eeeeee;display:flex;align-items:center;padding-left:12px;gap:8px;font-size:27px;color:var(--brand);font-weight:400}
.brand-dot{width:26px;height:26px;border-radius:50%;background:var(--brand)}
.nav{display:flex}
.nav a{color:var(--white);text-decoration:none;font-size:15px;height:51px;display:flex;align-items:center;justify-content:center;border-right:1px solid var(--brand-line)}
.panel{position:absolute;background:var(--panel);border:1px solid var(--panel-line)}
.label{color:var(--brand)}
.info{font-size:13.5px}
.info span{position:absolute}
.radio-row{position:absolute;left:17px;right:19px;height:45px;border-bottom:1px solid var(--panel-line);font-size:14px}
.radio-row:last-of-type{border-bottom:none}
.opt{position:absolute;top:50%;transform:translateY(-50%);display:flex;align-items:center;gap:7px}
.dot{width:17px;height:17px;border-radius:50%;border:1px solid var(--brand);background:var(--white);display:flex;align-items:center;justify-content:center}
.dot.on::after{content:"";width:9px;height:9px;border-radius:50%;background:var(--brand)}
.search{position:absolute;left:0;top:225px;width:463px;height:44px;background:var(--search);font-size:14px;display:flex;align-items:center;padding-left:23px}
.search-btn{position:absolute;right:-1px;top:0;width:52px;height:44px;background:var(--brand);display:flex;align-items:center;justify-content:center}
.grid{position:absolute;background:var(--panel);border:1px solid var(--panel-line);font-size:14px;overflow:hidden}
.grid-head{position:absolute;left:0;top:0;right:0;background:var(--brand);color:var(--white);font-size:14px}
.grid-head span,.cell{position:absolute;display:flex;align-items:center}
.row{position:absolute;left:0;height:32px;border-bottom:1px solid var(--row-line)}
.vline{position:absolute;width:1px;background:var(--panel-line)}
.vscroll{position:absolute;width:24px;background:var(--white)}
.hscroll{position:absolute;height:22px;background:var(--white)}
.thumb{position:absolute;background:var(--scroll)}
.arrowbox{position:absolute;width:20px;height:18px;display:flex;align-items:center;justify-content:center;background:#f3f3f3;border:1px solid #e2e2e2}
.field{position:absolute;background:var(--field);border:1px solid var(--panel-line);font-size:14px;padding:11px 0 0 11px}
.btn{position:absolute;display:flex;align-items:center;justify-content:center;border-bottom:2px solid rgba(0,0,0,.25)}
.btn-brand{background:var(--brand)}
.btn-muted{background:var(--muted-btn)}
.btn-text{color:var(--white);font-weight:700;font-size:14px}
.num{justify-content:center}
.rev{color:var(--brand)}
</style>
</head>
<body>
<div class="stage">
  <div class="app">
    <header class="topbar">
      <div class="brand"><span class="brand-dot"></span>Velmodane</div>
      <nav class="nav">
        <a href="#" style="width:104px">Home</a>
        <a href="#" style="width:86px">Task</a>
        <a href="#" style="width:113px">Reports</a>
        <a href="#" style="width:113px">Contact</a>
        <a href="#" style="width:105px">Setting</a>
      </nav>
    </header>
  </div>

  <!-- Section 1: proposal details -->
  <section class="panel info" style="left:75px;top:124px;width:465px;height:78px">
    <span class="label" style="left:23px;top:13px">Proposal Id</span><span style="left:104px;top:13px">:&nbsp; 1334235</span>
    <span class="label" style="left:231px;top:13px">Customer Id</span><span style="left:346px;top:13px">:&nbsp; 110399</span>
    <span style="left:23px;top:43px">Status</span><span style="left:104px;top:43px">:&nbsp; Incomplete</span>
    <span class="label" style="left:231px;top:43px">Customer Name</span><span style="left:346px;top:43px">:&nbsp; Velmodane Ltd</span>
  </section>

  <!-- Section 2: product filters -->
  <section class="panel" style="left:75px;top:222px;width:465px;height:271px">
    <div class="radio-row" style="top:2px">
      <label class="opt" style="left:4px"><span class="dot on"></span>Mobile</label>
      <label class="opt" style="left:154px"><span class="dot"></span>Fixed Line</label>
      <label class="opt" style="left:291px"><span class="dot"></span>Other Products</label>
    </div>
    <div class="radio-row" style="top:47px">
      <label class="opt" style="left:4px"><span class="dot on"></span>Q4</label>
      <label class="opt" style="left:88px"><span class="dot"></span>Valtora</label>
      <label class="opt" style="left:207px"><span class="dot"></span>NX</label>
      <label class="opt" style="left:290px"><span class="dot"></span>Tangerine</label>
    </div>
    <div class="radio-row" style="top:92px">
      <label class="opt" style="left:4px"><span class="dot"></span>New</label>
      <label class="opt" style="left:154px"><span class="dot"></span>Resign</label>
    </div>
    <div class="radio-row" style="top:137px;height:44px">
      <label class="opt" style="left:4px"><span class="dot"></span>12</label>
      <label class="opt" style="left:73px"><span class="dot"></span>24</label>
      <label class="opt" style="left:142px"><span class="dot"></span>36</label>
      <label class="opt" style="left:215px"><span class="dot"></span>48</label>
      <label class="opt" style="left:284px"><span class="dot"></span>60</label>
      <label class="opt" style="left:354px"><span class="dot"></span>Other</label>
    </div>
    <div class="radio-row" style="top:181px;border-bottom:none">
      <label class="opt" style="left:4px"><span class="dot on"></span>Share Plan</label>
      <label class="opt" style="left:128px"><span class="dot"></span>Single Plan</label>
      <label class="opt" style="left:254px"><span class="dot"></span>MBB</label>
      <label class="opt" style="left:342px"><span class="dot"></span>Add-On</label>
    </div>
    <div class="search">Search Product...
      <div class="search-btn"><svg width="24" height="24" viewBox="0 0 24 24"><circle cx="10" cy="10" r="7.5" fill="none" stroke="#fff" stroke-width="2.6"/><line x1="15.5" y1="15.5" x2="21.5" y2="21.5" stroke="#fff" stroke-width="3" stroke-linecap="round"/></svg></div>
    </div>
  </section>

  <!-- Section 3: tariff grid -->
  <section class="grid" style="left:75px;top:514px;width:465px;height:353px">
    <div class="grid-head" style="height:43px">
      <span style="left:23px;top:0;height:43px">TARRIF</span>
      <span style="left:298px;width:167px;top:0;height:43px;justify-content:center;border-left:1px solid var(--brand-line)">PRICE</span>
    </div>
    <div class="vline" style="left:297px;top:43px;height:288px"></div>
    <div class="row" style="top:43px;width:441px"><span class="cell" style="left:24px;height:32px">Business Single 300</span><span class="cell num" style="left:298px;width:143px;height:32px">19.03</span></div>
    <div class="row" style="top:75px;width:441px"><span class="cell" style="left:24px;height:32px">Business Single 600</span><span class="cell num" style="left:298px;width:143px;height:32px">25.03</span></div>
    <div class="row" style="top:107px;width:441px"><span class="cell" style="left:24px;height:32px">Business Single 900</span><span class="cell num" style="left:298px;width:143px;height:32px">19.03</span></div>
    <div class="row" style="top:139px;width:441px"><span class="cell" style="left:24px;height:32px">Business Single 1200</span><span class="cell num" style="left:298px;width:143px;height:32px">25.03</span></div>
    <div class="row" style="top:171px;width:441px"><span class="cell" style="left:24px;height:32px">Business Single 300</span><span class="cell num" style="left:298px;width:143px;height:32px">19.03</span></div>
    <div class="row" style="top:203px;width:441px"><span class="cell" style="left:24px;height:32px">Business Single 600</span><span class="cell num" style="left:298px;width:143px;height:32px">25.03</span></div>
    <div class="row" style="top:235px;width:441px"><span class="cell" style="left:24px;height:32px">Business Single 900</span><span class="cell num" style="left:298px;width:143px;height:32px">19.03</span></div>
    <div class="row" style="top:267px;width:441px"><span class="cell" style="left:24px;height:32px">Business Single 1200</span><span class="cell num" style="left:298px;width:143px;height:32px">25.03</span></div>
    <div class="row" style="top:299px;width:441px;border-bottom:none"><span class="cell" style="left:24px;height:32px">Business Single 1200</span><span class="cell num" style="left:298px;width:143px;height:32px">25.03</span></div>
    <div class="vscroll" style="left:441px;top:43px;height:288px">
      <div class="arrowbox" style="left:2px;top:0"><svg width="10" height="6"><path d="M1 5 L5 1 L9 5" fill="none" stroke="#aaa"/></svg></div>
      <div class="thumb" style="left:0;top:36px;width:23px;height:78px"></div>
      <div class="arrowbox" style="left:2px;bottom:0"><svg width="10" height="6"><path d="M1 1 L5 5 L9 1" fill="none" stroke="#aaa"/></svg></div>
    </div>
    <div class="hscroll" style="left:0;top:331px;width:441px">
      <div class="arrowbox" style="left:0;top:2px;width:18px"><svg width="6" height="10"><path d="M5 1 L1 5 L5 9" fill="none" stroke="#aaa"/></svg></div>
      <div class="thumb" style="left:38px;top:0;width:108px;height:22px"></div>
      <div class="arrowbox" style="right:0;top:2px;width:18px"><svg width="6" height="10"><path d="M1 1 L5 5 L1 9" fill="none" stroke="#aaa"/></svg></div>
    </div>
  </section>

  <!-- Section 4: product detail -->
  <section class="panel" style="left:580px;top:124px;width:465px;height:222px">
    <div class="field" style="left:14px;top:15px;width:175px;height:37px">Product</div>
    <div class="field" style="left:201px;top:15px;width:112px;height:37px">Qty</div>
    <div class="field" style="left:325px;top:15px;width:124px;height:37px">Total Cost</div>
    <div class="field" style="left:14px;top:62px;width:175px;height:37px">Reveneu %</div>
    <div class="field" style="left:201px;top:62px;width:112px;height:37px">Minutes</div>
    <div class="field" style="left:325px;top:62px;width:124px;height:37px">Texts</div>
    <div class="field" style="left:14px;top:108px;width:435px;height:56px">Data</div>
    <div class="btn btn-brand" style="left:177px;top:175px;width:51px;height:37px" aria-label="Product info">
      <svg width="12" height="24" viewBox="0 0 12 24"><circle cx="6" cy="3.5" r="3" fill="#fff"/><path d="M1 9 H8 V20 H11 V23 H1 V20 H4 V12 H1 Z" fill="#fff"/></svg>
    </div>
    <div class="btn btn-muted" style="left:236px;top:175px;width:51px;height:37px" aria-label="Add to basket">
      <svg width="26" height="22" viewBox="0 0 26 22"><path d="M8 8 L13 2 L18 8" fill="none" stroke="#fff" stroke-width="2"/><path d="M1 8 H25 V10 H23 L21 20 H5 L3 10 H1 Z" fill="none" stroke="#fff" stroke-width="2" stroke-linejoin="round"/><path d="M9 12 V18 M13 12 V18 M17 12 V18" stroke="#fff" stroke-width="1.8"/></svg>
    </div>
  </section>

  <!-- Section 5: basket -->
  <section class="grid" style="left:580px;top:367px;width:465px;height:164px">
    <div class="grid-head" style="height:43px">
      <span style="left:23px;top:0;height:43px">PRODUCT</span>
      <svg class="abs" style="left:159px;top:17px" width="8" height="10"><path d="M0 4 L4 0 L8 4 Z M0 6 L4 10 L8 6 Z" fill="#fff"/></svg>
      <span style="left:177px;width:70px;top:0;height:43px;justify-content:center;border-left:1px solid var(--brand-line)">TYPE</span>
      <span style="left:247px;width:82px;top:0;height:43px;justify-content:center;border-left:1px solid var(--brand-line)">PRICE</span>
      <span style="left:329px;width:64px;top:0;height:43px;justify-content:center;border-left:1px solid var(--brand-line)">QTY</span>
      <span style="left:393px;width:72px;top:0;height:43px;justify-content:center;border-left:1px solid var(--brand-line)">TOTAL</span>
    </div>
    <div class="vline" style="left:177px;top:43px;height:98px"></div>
    <div class="vline" style="left:247px;top:43px;height:98px"></div>
    <div class="vline" style="left:329px;top:43px;height:98px"></div>
    <div class="vline" style="left:392px;top:43px;height:98px"></div>
    <div class="row" style="top:44px;width:441px"></div>
    <div class="row" style="top:76px;width:441px"></div>
    <div class="row" style="top:108px;width:441px;border-bottom:none"></div>
    <div class="vscroll" style="left:441px;top:43px;height:98px">
      <div class="arrowbox" style="left:2px;top:0"><svg width="10" height="6"><path d="M1 5 L5 1 L9 5" fill="none" stroke="#aaa"/></svg></div>
      <div class="thumb" style="left:0;top:30px;width:23px;height:24px"></div>
      <div class="arrowbox" style="left:2px;bottom:0"><svg width="10" height="6"><path d="M1 1 L5 5 L9 1" fill="none" stroke="#aaa"/></svg></div>
    </div>
    <div class="hscroll" style="left:0;top:141px;width:441px">
      <div class="arrowbox" style="left:0;top:2px;width:18px"><svg width="6" height="10"><path d="M5 1 L1 5 L5 9" fill="none" stroke="#aaa"/></svg></div>
      <div class="thumb" style="left:38px;top:0;width:108px;height:22px"></div>
      <div class="arrowbox" style="right:0;top:2px;width:18px"><svg width="6" height="10"><path d="M1 1 L5 5 L1 9" fill="none" stroke="#aaa"/></svg></div>
    </div>
  </section>
  <div class="btn btn-brand btn-text" style="left:968px;top:541px;width:76px;height:32px">DELETE</div>

  <!-- Section 6: totals -->
  <section class="grid" style="left:580px;top:597px;width:465px;height:271px">
    <div class="grid-head" style="height:43px;font-size:13.5px;line-height:1.15">
      <span style="left:192px;width:74px;top:0;height:43px;justify-content:center">QTY</span>
      <span style="left:276px;width:74px;top:0;height:43px;justify-content:center;text-align:center">MOTHLY<br>COST</span>
      <span style="left:360px;width:95px;top:0;height:43px;justify-content:center;text-align:center">MOTHLY<br>REVENUE</span>
    </div>
    <div class="row" style="top:43px;width:465px"><span class="cell" style="left:25px;height:32px">Mobile Voice</span><span class="cell num" style="left:192px;width:74px;height:32px">0</span><span class="cell num" style="left:276px;width:74px;height:32px">0</span><span class="cell num rev" style="left:360px;width:95px;height:32px">0</span></div>
    <div class="row" style="top:75px;width:465px"><span class="cell" style="left:25px;height:32px">Mobile Data Only</span><span class="cell num" style="left:192px;width:74px;height:32px">0</span><span class="cell num" style="left:276px;width:74px;height:32px">0</span><span class="cell num rev" style="left:360px;width:95px;height:32px">0</span></div>
    <div class="row" style="top:107px;width:465px"><span class="cell" style="left:25px;height:32px">Mobile Total</span><span class="cell num" style="left:192px;width:74px;height:32px">0</span><span class="cell num" style="left:276px;width:74px;height:32px">0</span><span class="cell num rev" style="left:360px;width:95px;height:32px">0</span></div>
    <div class="row" style="top:139px;width:465px"><span class="cell" style="left:25px;height:32px">Fixed Line</span><span class="cell num" style="left:192px;width:74px;height:32px">-</span><span class="cell num" style="left:276px;width:74px;height:32px">0</span><span class="cell num rev" style="left:360px;width:95px;height:32px">0</span></div>
    <div class="row" style="top:171px;width:465px"><span class="cell" style="left:25px;height:32px">Other Prodaucts</span><span class="cell num" style="left:192px;width:74px;height:32px">-</span><span class="cell num" style="left:276px;width:74px;height:32px">0</span><span class="cell num rev" style="left:360px;width:95px;height:32px">0</span></div>
    <div class="row" style="top:203px;width:465px"><span class="cell" style="left:25px;height:32px">Total Monthly Cost</span><span class="cell num" style="left:192px;width:74px;height:32px">-</span><span class="cell num" style="left:276px;width:74px;height:32px">0</span><span class="cell num" style="left:360px;width:95px;height:32px">-</span></div>
    <div class="row" style="top:235px;width:465px;border-bottom:none"><span class="cell rev" style="left:25px;height:32px">Total Monthly Revenue</span><span class="cell num" style="left:192px;width:74px;height:32px">-</span><span class="cell num" style="left:276px;width:74px;height:32px">-</span><span class="cell num" style="left:360px;width:95px;height:32px">999999.00</span></div>
  </section>

  <div class="btn btn-brand" style="left:903px;top:895px;width:66px;height:41px" aria-label="Back">
    <svg width="32" height="20" viewBox="0 0 32 20"><path d="M0 10 L12 0 V6 H31 V14 H12 V20 Z" fill="#fff"/></svg>
  </div>
  <div class="btn btn-brand" style="left:979px;top:895px;width:66px;height:41px" aria-label="Next">
    <svg width="32" height="20" viewBox="0 0 32 20"><path d="M32 10 L20 0 V6 H1 V14 H20 V20 Z" fill="#fff"/></svg>
  </div>
</div>
</body>
</html>
```